Business Card Design Project

Basketball Training program

Offers: Travel Club Program - Camps - Clinics - Private Training

website: rivetbasketball.example
Phone Contact: Main Phone: 555-317-4826
Email: rivet.basketball@mailbox.example

Industry/Entity Type

Business

Contact Information for Business Card

Need one for the following coaches:
Marlo Quintrell - Boys & Girls Basketball Coach
Noweni Tasker - Girls Basketball Coach
Anselmo Duvray - Director/Head Coach
Hollis Ruk- Boys Basketball
Warren Olivash - Boys Basketball
Tomas Ferlanga - Boys Basketball
Kavin Sotherby- Boys Basketball/ Trainer
Al Varnock - Boys & Girls Basketball Coach

Basketball Training program Logo - one side

Logo on the corner
new one on the left (RB)
old one on the right (old one is with the rivet and basketball)

```html
<!DOCTYPE html>
<html lang="en">
<head>
<meta charset="utf-8">
<title>Rivet Basketball – Business Card</title>
<link rel="stylesheet" href="https://fonts.googleapis.com/css2?family=Open+Sans:wght@400;600&display=swap">
<style>
  :root {
    --backdrop: #3a3532;
    --card: #121212;
    --card-edge: #1f1f1f;
    --gold: #f4b21b;
    --ink: #f2f2f2;
    --muted: #cfcfcf;
    --divider: #5a5a5a;
  }
  * { box-sizing: border-box; margin: 0; padding: 0; }
  html, body {
    width: 1200px; height: 814px; overflow: hidden;
    background: var(--backdrop);
    font-family: "Open Sans", Arial, sans-serif;
  }
  .stage {
    position: relative; width: 1200px; height: 814px;
    display: flex; align-items: center; justify-content: center; gap: 60px;
  }
  .card {
    position: relative; width: 520px; height: 298px;
    background: var(--card);
    border: 1px solid var(--card-edge);
    border-radius: 3px;
    box-shadow: 0 10px 30px rgba(0,0,0,.45);
    color: var(--ink);
  }
  /* Front side */
  .card-front { display: flex; align-items: center; padding: 0 34px; }
  .brand {
    width: 200px; display: flex; align-items: center; gap: 12px;
  }
  .brand-dot {
    flex: none; width: 46px; height: 46px; border-radius: 50%;
    background: var(--gold);
  }
  .brand-name {
    font-weight: 600; font-size: 22px; line-height: 1.15; color: var(--ink);
  }
  .divider {
    width: 1px; height: 150px; margin: 0 26px 0 14px;
    background: linear-gradient(to bottom, transparent, var(--divider), transparent);
  }
  .contact { display: flex; flex-direction: column; }
  .person-name { color: var(--gold); font-weight: 600; font-size: 17px; }
  .person-role { font-size: 13px; color: var(--ink); margin: 4px 0 10px; }
  .contact-list { list-style: none; }
  .contact-list li {
    display: flex; align-items: center; gap: 8px;
    font-size: 12.5px; color: var(--ink); line-height: 1.6;
  }
  .contact-list svg { width: 12px; height: 12px; flex: none; fill: var(--gold); }
  /* Back side */
  .card-back { padding: 40px 34px; }
  .back-marks {
    position: absolute; top: 42px; left: 120px;
    display: flex; align-items: center; gap: 26px;
  }
  .mark-initials {
    width: 108px; height: 108px; border-radius: 50%;
    border: 3px solid var(--ink);
    display: flex; align-items: center; justify-content: center;
    font-weight: 600; font-size: 44px; color: var(--ink);
  }
  .back-brand { display: flex; align-items: center; gap: 10px; }
  .back-brand .brand-dot { width: 38px; height: 38px; }
  .back-brand .brand-name { font-size: 20px; }
  .offers {
    position: absolute; right: 30px; bottom: 34px;
    font-size: 12.5px; color: var(--muted);
  }
  .offers-label { color: var(--gold); font-weight: 600; }
</style>
</head>
<body>
<main class="stage">
  <section class="card card-front">
    <div class="brand">
      <span class="brand-dot"></span>
      <span class="brand-name">Rivet<br>Basketball</span>
    </div>
    <div class="divider"></div>
    <div class="contact">
      <p class="person-name">Marlo Quintrell</p>
      <p class="person-role">Boys &amp; Girls Basketball Coach</p>
      <ul class="contact-list">
        <li>
          <svg viewBox="0 0 24 24" aria-hidden="true"><path d="M6.6 10.8a15.1 15.1 0 0 0 6.6 6.6l2.2-2.2c.3-.3.7-.4 1-.2 1.1.4 2.3.6 3.6.6.6 0 1 .4 1 1V20c0 .6-.4 1-1 1A17 17 0 0 1 3 4c0-.6.4-1 1-1h3.5c.6 0 1 .4 1 1 0 1.3.2 2.5.6 3.6.1.3 0 .7-.2 1z"/></svg>
          555-317-4826
        </li>
        <li>
          <svg viewBox="0 0 24 24" aria-hidden="true"><path d="M2 5h20v14H2zm2 2v.4l8 5 8-5V7zm0 2.8V17h16V9.8l-8 5z"/></svg>
          rivet.basketball@mailbox.example
        </li>
        <li>
          <svg viewBox="0 0 24 24" aria-hidden="true"><path d="M12 2a10 10 0 1 0 0 20 10 10 0 0 0 0-20zm6.9 6h-3a15 15 0 0 0-1.3-3.9A8 8 0 0 1 18.9 8zM12 4c.8 1.2 1.5 2.5 1.9 4h-3.8c.4-1.5 1.1-2.8 1.9-4zM4.3 14a8 8 0 0 1 0-4h3.4a16 16 0 0 0 0 4zm.8 2h3a15 15 0 0 0 1.3 3.9A8 8 0 0 1 5.1 16zM8 8H5.1a8 8 0 0 1 4.3-3.9A15 15 0 0 0 8 8zm4 12c-.8-1.2-1.5-2.5-1.9-4h3.8c-.4 1.5-1.1 2.8-1.9 4zm2.3-6H9.7a14 14 0 0 1 0-4h4.6a14 14 0 0 1 0 4zm.3 5.9a15 15 0 0 0 1.3-3.9h3a8 8 0 0 1-4.3 3.9zm1.7-5.9a16 16 0 0 0 0-4h3.4a8 8 0 0 1 0 4z"/></svg>
          rivetbasketball.example
        </li>
      </ul>
    </div>
  </section>

  <section class="card card-back">
    <div class="back-marks">
      <div class="mark-initials">RB</div>
      <div class="back-brand">
        <span class="brand-dot"></span>
        <span class="brand-name">Rivet<br>Basketball</span>
      </div>
    </div>
    <p class="offers"><span class="offers-label">Offers:</span> Travel Club Program - Camps - Clinics - Private Training</p>
  </section>
</main>
</body>
</html>
```